Webbanner-Design für Führungskräfte-Coach
Danke für Ihr Engagement und die einwandfreie Abwicklung.
Zielgruppe
Ich coache Führungskräfte und Teams im Verkauf. Haupt-Keywort und Haupt-Thema:
Führung im Vertrieb. Das Design soll Führungskräften mit Verkaufsfunktionen gefallen.
Aufgabenstellung
Gemäss Memo (Datei: RBF-Banner-Memo).

```html
<!DOCTYPE html>
<html lang="de">
<head>
<meta charset="utf-8">
<title>Rieder Coaching &amp; Training – Banner</title>
<link rel="stylesheet" href="https://fonts.googleapis.com/css2?family=Arimo:wght@400;700&display=swap">
<style>
  :root {
    --sky-top: #3f86d6;
    --sky-mid: #6aa6e6;
    --sky-low: #9cc6f0;
    --bar-blue: #3b6fd1;
    --bar-red: #b3171c;
    --band: rgba(45, 45, 45, 0.88);
    --white: #ffffff;
    --mark: #4a5a78;
    --portrait-light: #c9b6a8;
    --portrait-dark: #1f2026;
  }
  html, body {
    margin: 0;
    padding: 0;
    overflow: hidden;
    background: #ffffff;
  }
  .banner {
    position: relative;
    width: 1200px;
    height: 457px;
    overflow: hidden;
    font-family: "Arimo", Arial, sans-serif;
    color: var(--white);
  }
  .sky {
    position: absolute;
    inset: 0;
    background:
      radial-gradient(ellipse 260px 140px at 330px 230px, rgba(255,255,255,0.55), rgba(255,255,255,0) 70%),
      linear-gradient(180deg, var(--sky-top) 0%, var(--sky-mid) 55%, var(--sky-low) 100%);
  }
  .top-bar {
    position: absolute;
    top: 0;
    left: 0;
    width: 100%;
    height: 7px;
    display: flex;
  }
  .top-bar .blue { flex: 0 0 616px; background: var(--bar-blue); }
  .top-bar .red { flex: 1; background: var(--bar-red); }

  .brand {
    position: absolute;
    top: 32px;
    left: 40px;
    display: flex;
    align-items: center;
  }
  .brand-square {
    width: 66px;
    height: 66px;
    background: var(--mark);
    margin-right: 14px;
  }
  .brand-divider {
    width: 2px;
    height: 70px;
    background: rgba(255,255,255,0.85);
    margin-right: 10px;
  }
  .brand-name {
    line-height: 1.1;
  }
  .brand-name .name {
    display: block;
    font-size: 27px;
    font-weight: 700;
  }
  .brand-name .sub {
    display: block;
    font-size: 21px;
    font-weight: 400;
  }

  .contact {
    position: absolute;
    top: 47px;
    right: 34px;
    display: flex;
    gap: 32px;
    font-size: 21px;
    font-weight: 700;
  }
  .contact-item {
    display: flex;
    align-items: center;
    gap: 9px;
  }
  .contact-item svg { display: block; }

  .tagline-band {
    position: absolute;
    left: 0;
    bottom: 0;
    width: 100%;
    height: 73px;
    background: var(--band);
    display: flex;
    align-items: center;
  }
  .tagline {
    margin: 0 0 0 40px;
    font-size: 26px;
    font-weight: 700;
  }

  .portrait {
    position: absolute;
    left: 770px;
    top: 108px;
    width: 430px;
    height: 349px;
    border-radius: 120px 120px 0 0;
    background: linear-gradient(180deg, var(--portrait-light) 0%, #6b6566 38%, var(--portrait-dark) 70%);
  }
</style>
</head>
<body>
  <div class="banner">
    <div class="sky" role="img" aria-label="Blauer Himmel mit einer Wolke in Form eines nach oben zeigenden Pfeils"></div>
    <div class="top-bar"><span class="blue"></span><span class="red"></span></div>

    <div class="brand">
      <div class="brand-square"></div>
      <div class="brand-divider"></div>
      <div class="brand-name">
        <span class="name">Rieder</span>
        <span class="sub">Coaching &amp; Training GmbH</span>
      </div>
    </div>

    <div class="contact">
      <div class="contact-item">
        <svg width="18" height="18" viewBox="0 0 18 18" fill="none" stroke="#ffffff" stroke-width="1.6">
          <circle cx="9" cy="9" r="7.5"/>
          <ellipse cx="9" cy="9" rx="3.2" ry="7.5"/>
          <line x1="1.5" y1="9" x2="16.5" y2="9"/>
          <line x1="3" y1="5" x2="15" y2="5"/>
          <line x1="3" y1="13" x2="15" y2="13"/>
        </svg>
        <span>www.rbf.ch</span>
      </div>
      <div class="contact-item">
        <svg width="20" height="14" viewBox="0 0 20 14">
          <rect x="0" y="0" width="20" height="14" fill="#ffffff"/>
          <polyline points="0.5,0.5 10,8 19.5,0.5" fill="none" stroke="#6aa6e6" stroke-width="1.6"/>
        </svg>
        <span>Info@rbf.ch</span>
      </div>
    </div>

    <div class="tagline-band">
      <p class="tagline">Coach für Führungskräfte und Teams im Vertrieb</p>
    </div>

    <div class="portrait" role="img" aria-label="Porträt des Coachs im dunklen Sakko und hellblauen Hemd"></div>
  </div>
</body>
</html>
```